Flowy subpage design wanted for a modern tax/accounting firm in Switzerland

--- Introduction ---
We are a tax and accounting firm in Switzerland. We provide services for expats living in Switzerland, our service is quite exclusive and modern (digital).

We just relaunched our website www.fiscaverde.ch and are happy with the design, so the desired subpage (more details below) should of course fit in.

--- Main brief ---
Please see Word File attached. The page has to include the whole text (11 chapters). A very intuitive, flowy design on only one subpage (not one page per chapter) is a MUST. Also, it is key that the design is supporting the content of the individual chapters, so it would be advantageous if you'd have a good unterstanding of the text attached.

--- Further information ---
A similar example would be this one: https://www2.brennmark.com/ch/en/pages/tax/articles/living-working-switzerland.html

This one is similar in what concerns the content, but NOT what we are looking for designwise. It is very simple and looks "thrown together", just not aesthetically pleasing in our opinion.

--- Final thoughts ---
- If you blow our minds with your design, we will certainly have future work for you.
- Our clients are between 20-50 years old, well educated, high income / high wealth, English speaking and living in Switzerland.
- CI/CD information:
Fonts
Montserrat regular / medium italic / bold
Colors
White #ffffffff
Darkblue #0a2b46
Darkblue 25% #b5bfc8
Darkblue 50% #8595a4
Greenblue #0d4261

We are looking forward to your designs!
Updates

Thank you very much for the submitted designs and your efforts. Unfortunately, none of the designs meet our expectations so far. Please note the following: - Designs that do not take CI into account will not be looked at more closely. - We have received many simple designs with very simple structure and accordion elements. But more important than the simple structure is an eye-catching design! Make it flowy and beautiful - We don't want pictures of Swiss vehicles, passes or other pictures that don't actively support the text. If you can make an illustration that really fits the context, fine, otherwise better leave it without. Thank you

Target Market(s)

Expats living in Switzerland. High income earners / high net worth individuals

Industry/Entity Type

tax/accounting

Number of Pages Required

1 page

Font styles to use
Other font styles liked:
• Montserrat

Colors
0054AA
0677BA
7BADD7
CADEEF
E8F1F8

Requirements
Must have
• based on general website design
Nice to have
• intuitive, flowy, attractive representation of much text
Should not have
• basic copy/paste of the text in sections :)

```html
<!DOCTYPE html>
<html lang="en">
<head>
<meta charset="utf-8">
<title>Living and working in Switzerland – Fiscaverde Advisory</title>
<link href="https://fonts.googleapis.com/css2?family=Montserrat:ital,wght@0,400;0,500;0,700;1,500&display=swap" rel="stylesheet">
<style>
  :root {
    --white: #ffffff;
    --darkblue: #0a2b46;
    --darkblue-25: #b5bfc8;
    --darkblue-50: #8595a4;
    --greenblue: #0d4261;
    --hero-grey: #e9ecef;
    --border: #c9d0d6;
    --text-muted: #7d8994;
  }
  * { box-sizing: border-box; margin: 0; padding: 0; }
  html, body { width: 1200px; height: 656px; overflow: hidden; background: var(--white); }
  body { font-family: "Montserrat", sans-serif; color: var(--darkblue); position: relative; }

  .hero-shapes { position: absolute; inset: 0; width: 1200px; height: 656px; }

  .site-header {
    position: absolute; top: 0; left: 0; width: 1200px; height: 55px;
    background: rgba(255,255,255,0.85);
  }
  .brand {
    position: absolute; left: 214px; top: 15px;
    display: flex; align-items: center; gap: 8px;
    font-weight: 500; font-size: 15px; letter-spacing: 0.06em;
    color: var(--darkblue); text-transform: uppercase; text-decoration: none;
  }
  .brand-dot { width: 24px; height: 24px; border-radius: 50%; border: 2px solid var(--darkblue); }
  .main-nav {
    position: absolute; top: 20px; left: 556px;
    display: flex; gap: 20px; font-size: 10px; color: var(--darkblue-50);
  }
  .main-nav a { color: inherit; text-decoration: none; }
  .main-nav .has-menu::after { content: "▾"; font-size: 8px; margin-left: 2px; }
  .calc-button {
    position: absolute; left: 1069px; top: 17px; width: 88px; height: 27px;
    background: var(--darkblue); color: var(--white);
    display: flex; align-items: center; justify-content: center; gap: 8px;
    font-size: 10px; text-decoration: none;
  }

  .hero-text { position: absolute; left: 214px; top: 158px; }
  .hero-eyebrow { font-size: 13px; color: var(--text-muted); margin-bottom: 10px; }
  .hero-title { font-size: 36px; line-height: 44px; font-weight: 700; color: var(--greenblue); }
  .hero-title span { display: block; font-weight: 400; color: var(--text-muted); }

  .chapter-tabs {
    position: absolute; left: 214px; top: 450px; width: 774px;
    display: grid; grid-template-columns: repeat(3, 1fr); grid-auto-rows: 36px;
    border-top: 1px solid var(--border); border-left: 1px solid var(--border);
  }
  .chapter-tabs a {
    display: flex; align-items: center; justify-content: center;
    border-right: 1px solid var(--border); border-bottom: 1px solid var(--border);
    font-size: 13px; color: var(--text-muted); text-decoration: none; white-space: nowrap;
  }
  .chapter-tabs a.is-active { background: var(--greenblue); color: var(--white); }

  .section-title {
    position: absolute; top: 640px; left: 0; width: 1200px; text-align: center;
    font-size: 34px; font-weight: 700; color: var(--darkblue);
  }
</style>
</head>
<body>
  <svg class="hero-shapes" viewBox="0 0 1200 656" aria-hidden="false">
    <defs>
      <linearGradient id="facade" x1="0" y1="0" x2="1" y2="1">
        <stop offset="0" stop-color="#c9c6bf"/>
        <stop offset="0.5" stop-color="#9ea3a6"/>
        <stop offset="1" stop-color="#5f6f7c"/>
      </linearGradient>
    </defs>
    <polygon points="0,55 800,55 800,337 0,382" fill="var(--hero-grey)"/>
    <polygon role="img" aria-label="Photo of a modern office building facade with rows of windows"
             points="803,24 1000,24 1200,240 1200,309 774,337 658,342" fill="url(#facade)"/>
    <polygon points="774,337 1200,309 1200,470" fill="var(--greenblue)"/>
  </svg>

  <header class="site-header">
    <a class="brand" href="#"><span class="brand-dot"></span>Fiscaverde Advisory</a>
    <nav class="main-nav">
      <a href="#">Home</a>
      <a href="#">Tax returns</a>
      <a href="#" class="has-menu">More services</a>
      <a href="#">Swiss tax guide</a>
      <a href="#">About us</a>
    </nav>
    <a class="calc-button" href="#">
      <svg width="12" height="14" viewBox="0 0 12 14" aria-hidden="true">
        <rect x="0.5" y="0.5" width="11" height="13" rx="1" fill="none" stroke="#fff"/>
        <rect x="2.5" y="2.5" width="7" height="3" fill="#fff"/>
        <g fill="#fff"><rect x="2.5" y="7" width="2" height="2"/><rect x="5" y="7" width="2" height="2"/><rect x="7.5" y="7" width="2" height="2"/>
        <rect x="2.5" y="10" width="2" height="2"/><rect x="5" y="10" width="2" height="2"/><rect x="7.5" y="10" width="2" height="2"/></g>
      </svg>
      Calculate
    </a>
  </header>

  <section class="hero-text">
    <p class="hero-eyebrow">About Switzerland</p>
    <h1 class="hero-title">Living and working<span>in Switzerland</span></h1>
  </section>

  <nav class="chapter-tabs">
    <a href="#" class="is-active">Life in Switzerland</a>
    <a href="#">Brief Overview of alpine country</a>
    <a href="#">Immigrating to Switzerland</a>
    <a href="#">labor law in Switzerland</a>
    <a href="#">Switzerland double tax agreements</a>
    <a href="#">Indirect taxes in Switzerland</a>
    <a href="#">Federal taxes in Switzerland</a>
    <a href="#">Rent and buy in Switzerland</a>
    <a href="#">Childcare in Switzerland</a>
    <a href="#">Public transportation in Switzerland</a>
    <a href="#">Recreation</a>
    <span></span>
  </nav>

  <h2 class="section-title">Life in Switzerland</h2>
</body>
</html>
```